Design a Website Mockup for domain Venthorquix.com

Design a website around [login to view URL] I want a website design that provides a simple, interactive game. No nudity.
Visitors, should they accept the challenge, put their sexuality detecting skills to the test. They will be presented with photos, and have to choose whether they are a female, or if they are infact a male in disguise. They will get a score, and then an option to share their score on social media sites. The actual structure of the game is up to you. Minimal design, with a non-instrusive space for advertising.

```html
<!DOCTYPE html>
<html lang="en">
<head>
<meta charset="utf-8">
<title>Venthorquix.com</title>
<link rel="stylesheet" href="https://fonts.googleapis.com/css2?family=Open+Sans:ital,wght@0,300;0,400;0,600;0,700;1,300;1,400&display=swap">
<style>
  :root {
    --sky-top: #7e2c4c;
    --sky-bottom: #d4512a;
    --band-top: #5e1a78;
    --band-bottom: #7a1f92;
    --footer: #3b1810;
    --footer-line: #d0561c;
    --logo-disc: #2b1119;
    --frame: #ffffff;
    --stage: #2a110c;
    --stage-top: #31140f;
    --login-a: #ffc928;
    --login-b: #f29e00;
    --signup-a: #29b3ea;
    --signup-b: #0f8fc8;
    --note-box: #3c1912;
    --text-light: #ffffff;
    --choice-a: #ffffff;
    --choice-b: #dcdcdc;
    --choice-text: #2a2a2a;
  }
  * { margin: 0; padding: 0; box-sizing: border-box; }
  html, body { width: 1200px; height: 960px; overflow: hidden; }
  body {
    position: relative;
    font-family: "Open Sans", Arial, sans-serif;
    color: var(--text-light);
    background: linear-gradient(180deg, var(--sky-top) 0%, var(--sky-bottom) 100%) top / 100% 567px no-repeat, var(--band-bottom);
  }
  .play-band {
    position: absolute; left: 0; top: 567px; width: 1200px; height: 351px;
    background: linear-gradient(160deg, var(--band-top) 0%, var(--band-bottom) 60%, #6c1b86 100%);
  }
  .site-footer {
    position: absolute; left: 0; top: 918px; width: 1200px; height: 42px;
    background: var(--footer);
    border-top: 7px solid var(--footer-line);
  }
  .copyright {
    position: absolute; right: 14px; top: 10px;
    font-size: 14px; color: var(--text-light);
  }
  .brand {
    position: absolute; left: 17px; top: 17px; width: 240px; height: 240px;
    border-radius: 50%; background: var(--logo-disc);
    display: flex; align-items: center; justify-content: center;
  }
  .brand-name { font-size: 29px; font-weight: 400; color: var(--text-light); }
  .account-btn {
    position: absolute; left: 0; width: 229px; height: 62px;
    border-radius: 0 31px 31px 0;
    display: flex; align-items: center;
    font-size: 29px; font-weight: 700; color: var(--text-light);
    box-shadow: 0 2px 3px rgba(0,0,0,.25);
  }
  .account-btn .label { width: 163px; padding-left: 26px; border-right: 2px solid rgba(0,0,0,.15); line-height: 62px; }
  .account-btn .arrow { flex: 1; display: flex; justify-content: center; }
  .btn-login { top: 289px; background: linear-gradient(180deg, var(--login-a), var(--login-b)); }
  .btn-signup { top: 373px; background: linear-gradient(180deg, var(--signup-a), var(--signup-b)); }
  .leaderboard-link {
    position: absolute; left: 43px; top: 457px; width: 193px; height: 87px;
    background: var(--note-box);
    box-shadow: 0 2px 4px rgba(0,0,0,.35);
    display: flex; align-items: center; justify-content: center; text-align: center;
    font-size: 18px; line-height: 24px;
  }
  .stats { position: absolute; left: 27px; width: 216px; text-align: center; font-weight: 300; }
  .stat-label { font-size: 34px; line-height: 40px; }
  .stat-value { font-size: 82px; line-height: 90px; }
  .timer { top: 597px; }
  .score { top: 763px; }
  .stats-rule { position: absolute; left: 27px; top: 750px; width: 216px; height: 1px; background: rgba(255,255,255,.7); }
  .photo-frame {
    position: absolute; left: 277px; top: 36px; width: 886px; height: 759px;
    background: var(--frame); padding: 16px;
  }
  .photo-slot {
    width: 100%; height: 100%;
    background: linear-gradient(180deg, var(--stage-top) 0, var(--stage-top) 151px, var(--stage) 151px);
    display: flex; align-items: center; justify-content: center; text-align: center;
    font-style: italic; font-weight: 300; font-size: 67px; line-height: 97px;
  }
  .choice {
    position: absolute; top: 812px; width: 280px; height: 85px;
    border-radius: 7px;
    background: linear-gradient(180deg, var(--choice-a), var(--choice-b));
    box-shadow: 0 3px 5px rgba(0,0,0,.35);
    display: flex; align-items: center; justify-content: center;
    font-style: italic; font-size: 45px; color: var(--choice-text);
  }
  .choice-lady { left: 393px; }
  .choice-ladyboy { left: 765px; }
</style>
</head>
<body>
  <div class="play-band"></div>

  <div class="brand"><span class="brand-name">Venthorquix.com</span></div>

  <div class="account-btn btn-login">
    <span class="label">Log In</span>
    <span class="arrow"><svg width="26" height="20" viewBox="0 0 26 20"><path d="M3 3l7 7-7 7M13 3l7 7-7 7" fill="none" stroke="#fff" stroke-width="3.5" stroke-linecap="round" stroke-linejoin="round"/></svg></span>
  </div>
  <div class="account-btn btn-signup">
    <span class="label">Sign Up</span>
    <span class="arrow"><svg width="26" height="20" viewBox="0 0 26 20"><path d="M3 3l7 7-7 7M13 3l7 7-7 7" fill="none" stroke="#fff" stroke-width="3.5" stroke-linecap="round" stroke-linejoin="round"/></svg></span>
  </div>

  <div class="leaderboard-link">Check out<br>the Leaderboard !</div>

  <div class="stats timer">
    <div class="stat-label">Time Left</div>
    <div class="stat-value">1:30</div>
  </div>
  <div class="stats-rule"></div>
  <div class="stats score">
    <div class="stat-label">Your Score is</div>
    <div class="stat-value">58</div>
  </div>

  <div class="photo-frame">
    <div class="photo-slot" role="img" aria-label="Photo to guess goes here">Your Image<br>Here</div>
  </div>

  <div class="choice choice-lady">Lady</div>
  <div class="choice choice-ladyboy">LadyBoy</div>

  <footer class="site-footer"><span class="copyright">Copyrights 2013 Venthorquix.com</span></footer>
</body>
</html>
```